Hello - we need a label design for our Corvane Medical Hair Loss supplement. It is a natural hair loss supplement for black/african american women to regrow new hair and help restore hair loss & thinning hair due to vitamin deficiencies, traction alopecia, etc. It is a science based efficacious supplement with a centuries old medicinal herbal formula.
Attached is the logo & files of other generic competition and also Black hair products for your perusal. The label has to be a upscale and have an ethnic flair to it. The product is clinically effective, leveraged by Ancient Wisdom and Modern Science. The front of the label should include the following:
Corvane Medical (logo)
Growth Accelerator
Advanced Women’s Hair Loss Formula
TRACTION ALOPECIA THERAPY
- Prevents hair loss & restores thinning, fragile hair
- Promotes Natural Hair Growth
- Strengthens Hair for less breakage
- Visibly increases hair density & thickness
- Thicker, Stronger, Longer, Hydrated hair
- Promotes Follicle regeneration & Hair Growth
Site-Specific for hair loss & stunted growth
60 capsules 30-day supply
Target Market(s)
Black/African American Women

```html
<!DOCTYPE html>
<html lang="en">
<head>
<meta charset="utf-8">
<title>Corvane Medical Growth Accelerator Label</title>
<link href="https://fonts.googleapis.com/css2?family=Bebas+Neue&family=Montserrat:wght@500&family=Roboto:wght@400&display=swap" rel="stylesheet">
<style>
  :root {
    --page-bg: #ffffff;
    --light-bg: #ffffff;
    --light-ink: #111111;
    --light-accent: #8a4a20;
    --dark-bg: #0b0706;
    --dark-ink: #ffffff;
    --dark-accent: #d98a3d;
  }
  * { margin: 0; padding: 0; box-sizing: border-box; }
  html, body { width: 1200px; height: 1052px; overflow: hidden; background: var(--page-bg); }
  body { position: relative; }

  .label {
    position: absolute;
    left: 153px;
    width: 889px;
    height: 371px;
    border-radius: 14px;
    background: var(--bg);
    color: var(--ink);
    box-shadow: 0 2px 5px rgba(0,0,0,0.35);
  }
  .label--light { top: 139px; --bg: var(--light-bg); --ink: var(--light-ink); --accent: var(--light-accent); }
  .label--dark  { top: 535px; --bg: var(--dark-bg);  --ink: var(--dark-ink);  --accent: var(--dark-accent); }

  .brand {
    position: absolute;
    left: 113px; top: 68px;
    width: 220px;
    display: flex; align-items: center; justify-content: center; gap: 10px;
    font-family: "Montserrat", sans-serif;
    font-weight: 500;
    font-size: 24px;
    color: var(--accent);
    white-space: nowrap;
  }
  .brand__dot { width: 12px; height: 12px; border-radius: 50%; background: var(--accent); flex: none; }

  .product-name {
    position: absolute;
    left: 0; width: 752px; top: 175px;
    text-align: center;
    font-family: "Bebas Neue", sans-serif;
    font-size: 34px;
    letter-spacing: 0.2px;
    color: var(--ink);
  }
  .label--light .product-name, .label--dark .product-name { width: 446px; }

  .tagline {
    position: absolute;
    left: 0; width: 446px; top: 233px;
    text-align: center;
    font-family: "Montserrat", sans-serif;
    font-weight: 500;
    font-size: 16.5px;
    letter-spacing: 0.3px;
    color: var(--accent);
  }

  .quantity { position: absolute; top: 293px; font-family: "Roboto", sans-serif; }
  .quantity--capsules { left: 117px; }
  .quantity--supply { left: 226px; }
  .label--dark .quantity--capsules { left: 111px; }
  .label--dark .quantity--supply { left: 220px; }
  .quantity__number {
    display: flex; align-items: center; gap: 8px;
    font-family: "Bebas Neue", sans-serif;
    font-size: 40px; line-height: 34px;
    color: var(--ink);
  }
  .quantity__number svg { fill: var(--accent); }
  .quantity__unit { font-size: 17.5px; color: var(--ink); margin-top: 3px; }

  .therapy-title {
    position: absolute;
    left: 540px; width: 247px; top: 44px;
    text-align: center;
    font-family: "Bebas Neue", sans-serif;
    font-size: 25px;
    color: var(--accent);
  }
  .therapy-rule {
    position: absolute;
    left: 540px; width: 247px; top: 87px;
    height: 1px; background: var(--accent);
  }
  .benefits {
    position: absolute;
    left: 473px; top: 106px;
    list-style: none;
    font-family: "Roboto", sans-serif;
    font-size: 15.8px;
    line-height: 19.9px;
    color: var(--ink);
  }
  .benefits li { position: relative; padding-left: 14px; white-space: nowrap; }
  .benefits li::before {
    content: ""; position: absolute; left: 0; top: 9px;
    width: 4px; height: 4px; background: var(--ink);
  }
  .site-note {
    position: absolute;
    left: 540px; width: 247px; top: 305px;
    text-align: center;
    font-family: "Roboto", sans-serif;
    font-size: 16px;
    color: var(--accent);
    white-space: nowrap;
  }
</style>
</head>
<body>

<section class="label label--light">
  <div class="brand"><span class="brand__dot"></span>Corvane Medical</div>
  <h1 class="product-name">Growth Accelerator</h1>
  <p class="tagline">Advanced Women’s Hair Loss Formula</p>
  <div class="quantity quantity--capsules">
    <div class="quantity__number">60
      <svg width="29" height="22" viewBox="0 0 29 22" aria-hidden="true">
        <rect x="1" y="3" width="9" height="17" rx="4.5"/>
        <rect x="12" y="5" width="9" height="17" rx="4.5" transform="rotate(-40 16.5 13.5)"/>
      </svg>
    </div>
    <div class="quantity__unit">capsules</div>
  </div>
  <div class="quantity quantity--supply">
    <div class="quantity__number">30
      <svg width="20" height="22" viewBox="0 0 20 22" aria-hidden="true">
        <rect x="4" y="0" width="2.5" height="4"/><rect x="13.5" y="0" width="2.5" height="4"/>
        <path d="M0 3h20v19H0z M2 8v12h16V8z" fill-rule="evenodd"/>
        <rect x="3.5" y="9.5" width="3" height="3"/><rect x="8.5" y="9.5" width="3" height="3"/><rect x="13.5" y="9.5" width="3" height="3"/>
        <rect x="3.5" y="14.5" width="3" height="3"/><rect x="8.5" y="14.5" width="3" height="3"/><rect x="13.5" y="14.5" width="3" height="3"/>
      </svg>
    </div>
    <div class="quantity__unit">day supply</div>
  </div>
  <h2 class="therapy-title">Traction Alopecia Therapy</h2>
  <div class="therapy-rule"></div>
  <ul class="benefits">
    <li>Prevents hair loss &amp; restores thinning, fragile hair</li>
    <li>Promotes Natural Hair Growth</li>
    <li>Strengthens Hair for less breakage</li>
    <li>Visibly increases hair density &amp; thickness</li>
    <li>Thicker, Stronger, Longer, Hydrated hair</li>
    <li>Promotes Follicle regeneration &amp; Hair Growth</li>
  </ul>
  <p class="site-note">Specific for hair loss &amp; stunted growth</p>
</section>

<section class="label label--dark">
  <div class="brand"><span class="brand__dot"></span>Corvane Medical</div>
  <h1 class="product-name">Growth Accelerator</h1>
  <p class="tagline">Advanced Women’s Hair Loss Formula</p>
  <div class="quantity quantity--capsules">
    <div class="quantity__number">60
      <svg width="29" height="22" viewBox="0 0 29 22" aria-hidden="true">
        <rect x="1" y="3" width="9" height="17" rx="4.5"/>
        <rect x="12" y="5" width="9" height="17" rx="4.5" transform="rotate(-40 16.5 13.5)"/>
      </svg>
    </div>
    <div class="quantity__unit">capsules</div>
  </div>
  <div class="quantity quantity--supply">
    <div class="quantity__number">30
      <svg width="20" height="22" viewBox="0 0 20 22" aria-hidden="true">
        <rect x="4" y="0" width="2.5" height="4"/><rect x="13.5" y="0" width="2.5" height="4"/>
        <path d="M0 3h20v19H0z M2 8v12h16V8z" fill-rule="evenodd"/>
        <rect x="3.5" y="9.5" width="3" height="3"/><rect x="8.5" y="9.5" width="3" height="3"/><rect x="13.5" y="9.5" width="3" height="3"/>
        <rect x="3.5" y="14.5" width="3" height="3"/><rect x="8.5" y="14.5" width="3" height="3"/><rect x="13.5" y="14.5" width="3" height="3"/>
      </svg>
    </div>
    <div class="quantity__unit">day supply</div>
  </div>
  <h2 class="therapy-title">Traction Alopecia Therapy</h2>
  <div class="therapy-rule"></div>
  <ul class="benefits">
    <li>Prevents hair loss &amp; restores thinning, fragile hair</li>
    <li>Promotes Natural Hair Growth</li>
    <li>Strengthens Hair for less breakage</li>
    <li>Visibly increases hair density &amp; thickness</li>
    <li>Thicker, Stronger, Longer, Hydrated hair</li>
    <li>Promotes Follicle regeneration &amp; Hair Growth</li>
  </ul>
  <p class="site-note">Specific for hair loss &amp; stunted growth</p>
</section>

</body>
</html>
```